RVM Flooring Flyer/Direct Mail

I need a flyer that will be distributed by letterboxing. this flyer will be offering free measure and quotes for supply and installation of timber, bamboo, and laminate flooring. The flyer will need to eye catching and professional looking.
The main purpose of the flyer is to generate appointments that will be followed up by a sales measure and quote team.

- Free Measure and Quote
Services:
- Remove and dispose of old floor coverings
- Pre installation floor repair
- New floor installation
- Free dust and clean on every new floor installation

I have some design files, logo and stock images, the flyer must not clash with the logo and business card.

You can use any image from Pextra Images as I have subscription with them.
https://images.pextrafoto.com/au/gallery

Here are the links to the Timber and Bamboo flooring supplier that I will be buying from and the third link is for the laminate flooring supplier. Note, this is for getting an idea of what products we will be supplying and installing, Do not use their images!

https://www.grainhaven.com.au/timber-flooring/
https://cantorvex.com.au/bamboo-flooring/
http://www.dalvorsurfaces.com.au/brands/tenmark-laminate/

Target Market(s)

Domestic home owners

Industry/Entity Type

Construction Company

Colors

Designer to choose colors to be used in the design.

Requirements
Must have
• Size: A6 or DL
Nice to have
• Timber: Spotted Gum, Eastern States Blackbutt, Jarrah, Marri, and a large collection of French Oak.
• Bamboo: Our Bamboo range of flooring is engineered to withstand the extremes of the Australian climate.
• Laminate: All our laminate range comes with a 25 year product warranty. Choose from a large range of patterns, colours and finishes.

```html
<!DOCTYPE html>
<html lang="en">
<head>
<meta charset="utf-8">
<title>RVM Flooring – Flyer Front and Back</title>
<link href="https://fonts.googleapis.com/css2?family=Montserrat:wght@400;500;600;700;800&display=swap" rel="stylesheet">
<style>
  :root {
    --bg-light: #f1f1f1;
    --bg-dark: #bdbdbd;
    --paper: #ffffff;
    --brown-dark: #4a2f1e;
    --brown-mid: #7a4a2b;
    --brown-band: rgba(92, 70, 58, 0.78);
    --wood-light: #c08050;
    --wood-deep: #6b3a1c;
    --red: #d33d26;
    --orange: #ef8c1d;
    --red-orange: #dc4527;
    --white: #ffffff;
    --cream: #f6ede4;
  }
  * { box-sizing: border-box; margin: 0; padding: 0; }
  html, body { width: 1200px; height: 1200px; overflow: hidden; }
  body {
    background: radial-gradient(ellipse at 50% 40%, var(--bg-light) 0%, #d9d9d9 60%, var(--bg-dark) 100%);
    font-family: "Montserrat", Arial, sans-serif;
    color: var(--white);
    position: relative;
  }
  .flyer {
    position: absolute;
    top: 338px;
    width: 380px;
    height: 524px;
    background: var(--paper);
    padding: 7px;
    box-shadow: 0 14px 24px rgba(0,0,0,0.18);
  }
  .flyer--back { left: 170px; }
  .flyer--front { left: 650px; }

  /* Back side */
  .back-grid { display: flex; flex-direction: column; gap: 3px; height: 100%; }
  .hero {
    position: relative; height: 136px;
    background: linear-gradient(180deg, #bfa58a 0%, #a07a58 45%, #7a4e2e 100%);
  }
  .hero-title {
    position: absolute; left: 0; right: 0; bottom: 0; height: 62px;
    background: var(--brown-band); padding: 12px 12px 0;
  }
  .brand-name { font-weight: 800; font-size: 22px; letter-spacing: 0.5px; line-height: 1; }
  .brand-tag { font-weight: 600; font-size: 8.6px; letter-spacing: 0.5px; margin-top: 6px; line-height: 1.35; }
  .logo-lockup {
    position: absolute; display: flex; align-items: center; gap: 6px;
    font-weight: 500; font-size: 9px; letter-spacing: 0.5px; color: var(--white);
  }
  .logo-lockup .logo-square { width: 14px; height: 14px; border: 1.5px solid var(--white); }
  .hero .logo-lockup { top: 22px; right: 12px; }

  .tiles { display: grid; grid-template-columns: repeat(3, 1fr); gap: 3px; height: 104px; }
  .tile-photo { height: 100%; }
  .tile-photo--hands { background: linear-gradient(135deg, #8b5a36 0%, #a66a3c 50%, #5c6470 100%); }
  .tile-photo--room { background: linear-gradient(180deg, #e6ddd0 0%, #c9a679 50%, #9a6a3c 100%); }
  .tile-photo--deck { background: linear-gradient(180deg, #d8d2cc 0%, #8e4a2c 45%, #a1532d 100%); }

  .ranges { display: grid; grid-template-columns: repeat(3, 1fr); gap: 3px; height: 72px; }
  .range { padding: 8px 8px 0; text-align: center; }
  .range--timber { background: var(--red); }
  .range--laminate { background: var(--orange); }
  .range--bamboo { background: var(--red-orange); }
  .range h3 { font-weight: 700; font-size: 13px; margin-bottom: 6px; }
  .range p { font-size: 5.4px; line-height: 1.4; }

  .info { display: grid; grid-template-columns: 1fr 1fr; gap: 4px; height: 104px; margin-top: 1px; }
  .about { background: linear-gradient(160deg, var(--brown-mid), #a4582c 60%, #8a4423); padding: 10px 9px 0; text-align: center; }
  .services { background: linear-gradient(160deg, #a06a44, var(--brown-mid)); padding: 10px 9px 0; }
  .info h3 { font-weight: 700; font-size: 11px; text-align: center; margin-bottom: 6px; }
  .about p { font-size: 5.2px; font-weight: 600; line-height: 1.45; }
  .service-list { list-style: none; }
  .service-list li { display: flex; align-items: center; gap: 7px; font-size: 5.2px; font-weight: 600; line-height: 1.3; margin-bottom: 4px; }
  .service-list li::before { content: ""; flex: none; width: 7px; height: 7px; border-radius: 50%; background: var(--white); }

  .cta {
    flex: 1; margin-top: 1px;
    background: linear-gradient(180deg, #6b4630 0%, var(--brown-dark) 100%);
    text-align: center; padding-top: 14px;
    font-weight: 700; font-size: 13.5px; line-height: 1.32; letter-spacing: 0.3px;
  }

  /* Front side */
  .front-photo {
    position: relative; height: 100%;
    background: linear-gradient(180deg, #6e5a3e 0%, #8d6a3e 30%, #6a4a2e 50%, #8a552c 70%, #b2764a 85%, #5a3418 100%);
  }
  .front-logo {
    position: absolute; top: 13px; right: 13px; width: 125px; height: 82px;
    background: rgba(120, 110, 105, 0.55);
  }
  .front-logo .logo-lockup { left: 14px; top: 34px; font-size: 9.5px; }
  .front-band {
    position: absolute; left: 0; right: 0; top: 190px; height: 124px;
    background: var(--brown-band); text-align: center; padding-top: 34px;
  }
  .front-band .brand-name { font-size: 34px; }
  .front-band .brand-tag { font-size: 10.5px; margin-top: 6px; }
  .front-offer {
    position: absolute; left: 0; right: 0; bottom: 0; height: 44px;
    background: rgba(90, 66, 54, 0.85);
    display: flex; align-items: center; justify-content: center;
    font-weight: 700; font-size: 15.5px; letter-spacing: 0.3px;
  }
</style>
</head>
<body>

<section class="flyer flyer--back" aria-label="Flyer back">
  <div class="back-grid">
    <header class="hero" role="img" aria-label="Photo of a bright living room with a polished timber floor and rug">
      <div class="logo-lockup"><span class="logo-square"></span>RVM FLOORING</div>
      <div class="hero-title">
        <h1 class="brand-name">RVM FLOORING</h1>
        <p class="brand-tag">BAMBOO,TIMBER &amp; LAMINATE FLOORING<br>SUPPLIERS &amp; INSTALLERS</p>
      </div>
    </header>

    <div class="tiles">
      <div class="tile-photo tile-photo--hands" role="img" aria-label="Photo of an installer laying a timber floor board"></div>
      <div class="tile-photo tile-photo--room" role="img" aria-label="Photo of an empty room with a laminate floor"></div>
      <div class="tile-photo tile-photo--deck" role="img" aria-label="Photo of an open living area with a bamboo floor"></div>
    </div>

    <div class="ranges">
      <div class="range range--timber">
        <h3>Timber:</h3>
        <p>Spotted Gum, Eastern States Blackbutt, Jarrah, Marri, and a large collection of French Oak.</p>
      </div>
      <div class="range range--laminate">
        <h3>Laminate:</h3>
        <p>All our laminate range comes with a 25 year product warranty. Choose from a large range of patterns, colours and finishes.</p>
      </div>
      <div class="range range--bamboo">
        <h3>Bamboo:</h3>
        <p>Our Bamboo range of flooring is engineered to withstand the extremes of the Australian climate.</p>
      </div>
    </div>

    <div class="info">
      <div class="about">
        <h3>WHO WE ARE?</h3>
        <p>At RVM flooring we specialise in prefinished timber, bamboo and laminate flooring. We strive to provide a unique and professional experience to all our customers. Our goal is to provide the highest standard in customer service, integrity, quality and value for money. As a family business we understand the importance of relationship and seek to make your experience one you will be pleased you made.</p>
      </div>
      <div class="services">
        <h3>SERVICES</h3>
        <ul class="service-list">
          <li>Remove and dispose of old floor coverings</li>
          <li>Pre installation floor repair</li>
          <li>New floor installation</li>
          <li>Free dust and clean on every new floor installation</li>
        </ul>
      </div>
    </div>

    <footer class="cta">
      CALL US TODAY TO VIEW OUR<br>RANGE OF PRODUCTS<br>(08) 9412 7083
    </footer>
  </div>
</section>

<section class="flyer flyer--front" aria-label="Flyer front">
  <div class="front-photo" role="img" aria-label="Photo of a dining chair on a glossy timber floor beside sunny glass doors">
    <div class="front-logo">
      <div class="logo-lockup"><span class="logo-square"></span>RVM FLOORING</div>
    </div>
    <div class="front-band">
      <h1 class="brand-name">RVM FLOORING</h1>
      <p class="brand-tag">BAMBOO,TIMBER &amp; LAMINATE FLOORING<br>SUPPLIERS &amp; INSTALLERS</p>
    </div>
    <div class="front-offer">Free Measure and Quote</div>
  </div>
</section>

</body>
</html>
```